" A VORA SAN é uma empresa de engenharia especializada na manutençao de equipamentos biomédicos e no desenvolvimento de soluçoes para os diversos serviços de saúde "

```html
<!DOCTYPE html>
<html lang="pt-BR">
<head>
<meta charset="utf-8">
<title>VORA SAN – Placa de identificação</title>
<link rel="stylesheet" href="https://fonts.googleapis.com/css2?family=Questrial&display=swap">
<style>
  :root {
    --page-bg: #ececec;
    --plate-bg: #ffffff;
    --brand-red: #e2202b;
    --steel-grey: #b4b6b9;
    --text-dark: #2b2b2b;
    --text-muted: #8a8a8a;
  }
  html, body {
    margin: 0;
    padding: 0;
    width: 1200px;
    height: 1200px;
    overflow: hidden;
    background: var(--page-bg);
    font-family: "Questrial", Arial, sans-serif;
  }
  .canvas {
    position: relative;
    width: 1200px;
    height: 1200px;
  }
  .door-plate {
    position: absolute;
    left: 100px;
    top: 493px;
    width: 1000px;
    height: 214px;
    background: var(--plate-bg);
    border-radius: 14px;
    box-shadow: 0 6px 18px rgba(0,0,0,0.18);
    overflow: hidden;
  }
  .accent-band {
    position: absolute;
    right: 0;
    top: 0;
    width: 200px;
    height: 100%;
    background: var(--brand-red);
  }
  .accent-disc {
    position: absolute;
    left: 700px;
    top: -8px;
    width: 230px;
    height: 230px;
    border-radius: 50%;
    background: var(--steel-grey);
  }
  .brand {
    position: absolute;
    left: 36px;
    top: 76px;
  }
  .brand-name {
    display: flex;
    align-items: center;
    gap: 12px;
    color: var(--brand-red);
    font-size: 42px;
    line-height: 1;
    letter-spacing: 1px;
  }
  .brand-dot {
    width: 34px;
    height: 34px;
    border-radius: 50%;
    background: var(--steel-grey);
  }
  .brand-tagline {
    margin: 6px 0 0 47px;
    font-size: 11px;
    color: var(--text-muted);
    letter-spacing: 1px;
  }
  .contact {
    position: absolute;
    left: 383px;
    top: 84px;
    font-size: 21px;
    line-height: 25px;
    color: var(--text-dark);
  }
  .contact p { margin: 0; }
  .holder {
    position: absolute;
    left: 493px;
    top: 172px;
    font-size: 22px;
    color: var(--text-dark);
  }
</style>
</head>
<body>
  <main class="canvas">
    <section class="door-plate">
      <div class="accent-band"></div>
      <div class="accent-disc"></div>

      <div class="brand">
        <div class="brand-name"><span class="brand-dot"></span>VORA SAN</div>
        <div class="brand-tagline">engenharia biomédica</div>
      </div>

      <div class="contact">
        <p>Telefone:0000-0000</p>
        <p>Celular:0000-0000</p>
        <p>Email:contato@vorasan.com.br</p>
      </div>

      <div class="holder">Nome | Função</div>
    </section>
  </main>
</body>
</html>
```